furniture and home contents restoration

I need to list the services that we perform in our studio.
we serve the general public as well as the insurance/ remediation industry

```html
<!DOCTYPE html>
<html lang="en">
<head>
<meta charset="utf-8">
<title>Keystone Renewers – Business Card</title>
<link href="https://fonts.googleapis.com/css2?family=Source+Sans+3:wght@400;600;700&display=swap" rel="stylesheet">
<style>
  :root{
    --bg:#e4e4e4;
    --navy:#1d2c35;
    --card-light:#f1f1f2;
    --grey-band:#8a8b8e;
    --ink-light:#eef1f2;
    --ink-muted:#6b6d70;
  }
  *{margin:0;padding:0;box-sizing:border-box}
  html,body{width:1200px;height:1200px;overflow:hidden;background:var(--bg)}
  body{position:relative;font-family:"Source Sans 3",sans-serif}
  .card{position:absolute;left:263px;width:682px;height:390px;border-radius:34px;overflow:hidden;box-shadow:0 14px 22px rgba(0,0,0,.18)}
  .card--back{top:165px;background:var(--navy);color:var(--ink-light)}
  .card--front{top:654px;background:var(--card-light)}

  .services{position:absolute;top:84px;left:48px;right:20px;display:flex}
  .services ul{list-style:none;font-size:16.3px;line-height:19.6px}
  .services ul:first-child{width:303px}
  .services li{display:flex;align-items:center;gap:7px;white-space:nowrap}
  .services svg{width:14px;height:8px;flex:none}
  .inspection{position:absolute;top:319px;left:0;right:0;text-align:center;font-size:16.3px;line-height:20px}
  .inspection strong{font-weight:700}

  .brand{position:absolute;top:78px;left:0;right:0;text-align:center;color:var(--navy)}
  .brand-name{display:inline-flex;align-items:center;gap:12px;font-weight:700;font-size:40px;line-height:44px}
  .brand-mark{width:22px;height:22px;background:var(--navy)}
  .brand-tag{font-weight:400;font-size:16px;color:var(--ink-muted);margin-top:8px}

  .band{position:absolute;top:206px;left:0;right:0;height:109px;display:flex;gap:4px}
  .band-person{width:339px;background:var(--navy);color:#fff;text-align:right;padding:14px 32px 0 0}
  .person-name{font-weight:600;font-size:21px;line-height:26px;margin-bottom:12px}
  .person-address{font-size:15.5px;line-height:20px;color:#e8ecee}
  .band-contact{flex:1;background:var(--grey-band);color:#fff;padding:14px 0 0 32px;list-style:none;font-size:15.5px;line-height:19.6px}
  .band-contact li{display:flex;align-items:center;gap:9px}
  .band-contact svg{width:13px;height:13px;flex:none}
  .footer-line{position:absolute;top:340px;left:0;right:0;text-align:center;font-size:15.6px;color:var(--ink-muted)}
</style>
</head>
<body>
  <svg width="0" height="0" style="position:absolute">
    <symbol id="pointer" viewBox="0 0 14 8"><path d="M1 4.5h8.5M9.5 2.2h3.5M9.5 4.5h2.5M1 2.2c1.5-1.4 4-1.6 8.5 0M1 6.5h8" stroke="#e6ebed" stroke-width="1" fill="none" stroke-linecap="round"/></symbol>
  </svg>

  <section class="card card--back" aria-label="Services">
    <div class="services">
      <ul>
        <li><svg><use href="#pointer"/></svg>Antique Repair and Restoration</li>
        <li><svg><use href="#pointer"/></svg>Art Cleaning and Remounting</li>
        <li><svg><use href="#pointer"/></svg>Art and Mirror Frame Repair</li>
        <li><svg><use href="#pointer"/></svg>Chandelier Cleaning and Restoration</li>
        <li><svg><use href="#pointer"/></svg>Document Restoration</li>
        <li><svg><use href="#pointer"/></svg>Glass, Ceramic and Mirror Repair</li>
        <li><svg><use href="#pointer"/></svg>Hardware Repair and Restoration</li>
        <li><svg><use href="#pointer"/></svg>Kitchen Removal and Reinstallation</li>
        <li><svg><use href="#pointer"/></svg>Lamp Cleaning and Restoration</li>
        <li><svg><use href="#pointer"/></svg>Lamp Shade Replacement</li>
      </ul>
      <ul>
        <li><svg><use href="#pointer"/></svg>Metal Polishing and Restoration</li>
        <li><svg><use href="#pointer"/></svg>Odor Removal and Ozone Services</li>
        <li><svg><use href="#pointer"/></svg>Photo Restoration</li>
        <li><svg><use href="#pointer"/></svg>Upholstery Cleaning and Deodorizing</li>
        <li><svg><use href="#pointer"/></svg>In-House Upholstery and Reupholstery</li>
        <li><svg><use href="#pointer"/></svg>Rug Cleaning and Restoration</li>
        <li><svg><use href="#pointer"/></svg>Musical Instrument Restoration</li>
        <li><svg><use href="#pointer"/></svg>Window Treatment Repair/ Restoration</li>
        <li><svg><use href="#pointer"/></svg>Leather Restoration and Replacement</li>
        <li><svg><use href="#pointer"/></svg>Piano Restoration and Repair</li>
      </ul>
    </div>
    <p class="inspection"><strong>On-Site Inspections and Desk Review Services</strong><br>Assessment Reports and Estimates for Repair and Restoration</p>
  </section>

  <section class="card card--front" aria-label="Contact">
    <div class="brand">
      <div class="brand-name"><span class="brand-mark"></span>Keystone Renewers</div>
      <div class="brand-tag">Home Contents Restoration</div>
    </div>
    <div class="band">
      <div class="band-person">
        <div class="person-name">Daniel Moretti</div>
        <div class="person-address">82 Linden Brook Rd.<br>Ashford, NY 10590</div>
      </div>
      <ul class="band-contact">
        <li><svg viewBox="0 0 14 14"><path d="M3 1.5l2 2.6-1.2 1.5c.8 1.7 2 2.9 3.6 3.7l1.5-1.2 2.6 2-1.2 2C6 11.8 2.2 8 1 3z" fill="#fff"/></svg>555.201.4800</li>
        <li><svg viewBox="0 0 14 14"><rect x="3.5" y="1" width="7" height="12" rx="1.2" fill="none" stroke="#fff" stroke-width="1.3"/><circle cx="7" cy="11" r=".8" fill="#fff"/></svg>555.316.2947</li>
        <li><svg viewBox="0 0 14 14"><rect x="4" y="1" width="6" height="3.5" fill="#fff"/><rect x="1" y="5" width="12" height="5" rx="1" fill="#fff"/><rect x="4" y="8.5" width="6" height="4.5" fill="#fff" stroke="#8a8b8e" stroke-width=".8"/></svg>555.201.4855</li>
        <li><svg viewBox="0 0 14 14"><rect x="1" y="3" width="12" height="8" fill="#fff"/><path d="M1 3l6 4.5L13 3" fill="none" stroke="#8a8b8e" stroke-width="1"/></svg>keystone@mailbox.com</li>
      </ul>
    </div>
    <p class="footer-line">Serving The General Public and The Insurance Industry for Over 40 Years</p>
  </section>
</body>
</html>
```